Label for a bottle of Gin soon to launch in the UK.

We need a label for a gin called Marbury Gin. It is very important that the label does not infringe any copyrights of the football club so please avoid the colour blue or anything related to football or the club. The example bottle below shows the bottle that we will be using. The gin will be clear not pink, the use of gold on the label is encouraged.
Should not infringe on the brand shown in the example image.

Industry/Entity Type

Club

Font styles to use
Sans Serif

Requirements
Must have
• Here is a link to the bottle that the label must fit onto https://www.vessel-depot-example.co.uk/Glass-bottles/Glass-bottles/700ml-glass-bottles/700ml-clear-glass-bottle-Quilora.html
Should not have
• No use of blue or anything related to football or Halcombe Rowing Society or Stonewrens. Avoid Red also. White, gold and black should be primary colours used

```html
<!DOCTYPE html>
<html lang="en">
<head>
<meta charset="utf-8">
<title>Marbury Gin – Bottle Label</title>
<link href="https://fonts.googleapis.com/css2?family=Rye&family=Old+Standard+TT:wght@700&family=Montserrat:wght@500;600&family=Pinyon+Script&display=swap" rel="stylesheet">
<style>
  :root {
    --backdrop: #060606;
    --paper: #e3eae1;
    --ink: #26242e;
    --ink-soft: #5c5967;
    --gold: #b8913a;
    --gold-deep: #9c7a2c;
    --sepia: #c9b99a;
    --rule: #9a9c98;
  }
  html, body {
    margin: 0;
    width: 1200px;
    height: 1200px;
    overflow: hidden;
    background: var(--backdrop);
  }
  .label {
    position: absolute;
    left: 190px;
    top: 45px;
    width: 820px;
    height: 1110px;
    display: block;
  }
  .distillery { font-family: "Old Standard TT", Georgia, serif; font-weight: 700; font-size: 30px; letter-spacing: 5px; fill: var(--ink-soft); }
  .brand-word { font-family: "Rye", Georgia, serif; fill: var(--ink); }
  .brand-gin { font-family: "Rye", Georgia, serif; fill: var(--ink); }
  .brand-gin .first { fill: var(--ink-soft); }
  .detail { font-family: "Montserrat", Arial, sans-serif; font-weight: 600; font-size: 22px; letter-spacing: 3px; fill: var(--ink); }
  .origin { font-family: "Montserrat", Arial, sans-serif; font-weight: 600; font-size: 34px; letter-spacing: 4px; fill: var(--gold); }
  .meta { font-family: "Montserrat", Arial, sans-serif; font-weight: 500; font-size: 15px; letter-spacing: 1px; fill: var(--ink-soft); }
  .meta-small { font-family: "Montserrat", Arial, sans-serif; font-weight: 600; font-size: 11px; letter-spacing: 1.5px; fill: var(--ink-soft); }
  .strength { font-family: "Old Standard TT", Georgia, serif; font-weight: 700; font-size: 34px; fill: var(--ink); }
  .tagline { font-family: "Pinyon Script", cursive; font-size: 50px; fill: var(--gold-deep); }
  .maker-mark { font-family: "Montserrat", Arial, sans-serif; font-weight: 600; font-size: 18px; letter-spacing: 2px; fill: var(--gold); }
</style>
</head>
<body>
<svg class="label" viewBox="0 0 820 1110" xmlns="http://www.w3.org/2000/svg">
  <defs>
    <pattern id="scallop" width="20" height="20" patternUnits="userSpaceOnUse">
      <circle cx="10" cy="10" r="10" fill="#e3eae1"/>
    </pattern>
  </defs>

  <g class="paper">
    <rect x="0" y="10" width="820" height="1090" fill="var(--paper)"/>
    <rect x="0" y="0" width="820" height="20" fill="url(#scallop)"/>
    <rect x="0" y="1090" width="820" height="20" fill="url(#scallop)"/>
  </g>

  <text class="distillery" x="410" y="220" text-anchor="middle">ASHGROVE DISTILLERY</text>

  <text class="brand-word" x="30" y="440" font-size="190" textLength="760" lengthAdjust="spacingAndGlyphs">MARBURY</text>

  <text class="brand-gin" x="170" y="725" font-size="290" textLength="470" lengthAdjust="spacingAndGlyphs"><tspan class="first">G</tspan>IN</text>

  <text class="detail" x="410" y="775" text-anchor="middle">8 FINE BOTANICALS</text>
  <text class="origin" x="410" y="820" text-anchor="middle">LONDON, ENGLAND</text>
  <text class="detail" x="410" y="862" text-anchor="middle">CAREFULLY BLENDED</text>

  <rect x="18" y="770" width="120" height="262" rx="6" fill="var(--sepia)" opacity="0.45" role="img" aria-label="Engraved illustration of a gentleman under an umbrella beside a small cask"/>

  <g class="maker-seal">
    <circle cx="722" cy="820" r="70" fill="none" stroke="var(--gold)" stroke-width="3"/>
    <text class="maker-mark" x="722" y="816" text-anchor="middle">MARBURY</text>
    <text class="maker-mark" x="722" y="840" text-anchor="middle">GIN CO.</text>
  </g>

  <line x1="150" y1="905" x2="790" y2="905" stroke="var(--rule)" stroke-width="1.5" stroke-dasharray="2 4"/>

  <text class="meta" x="150" y="945">BATCH# 0003</text>
  <text class="tagline" x="410" y="952" text-anchor="middle">Bad luck gin</text>
  <text class="meta" x="790" y="945" text-anchor="end">BOTTLE# 0622</text>

  <text class="meta-small" x="150" y="1020">DISTILLER</text>
  <rect x="150" y="1030" width="100" height="20" rx="4" fill="var(--sepia)" opacity="0.45" role="img" aria-label="Distiller's handwritten signature"/>
  <text class="meta-small" x="262" y="1020">ALCOHOL</text>
  <text class="strength" x="342" y="1025">40%VOL</text>
  <line x1="488" y1="990" x2="488" y2="1035" stroke="var(--rule)" stroke-width="1.5"/>
  <text class="meta-small" x="502" y="1020">VOLUMEN</text>
  <text class="strength" x="588" y="1025">70 CL</text>
</svg>
</body>
</html>
```